Brookmere Osteopathy and dry needling business card

Business card for Brookmere Osteopathy and Dry Needling.

Industry/Entity Type

Health

Contact Information for Business Card

I do not have a phone number yet. I also do not have an email address yet. The physical address is: 47 Lindcombe Lane Brookmere The website is: www.brookmereosteopathyclinic.example My details are: Dr Marcus Penhallow, Osteopath (B.Clin.Sci (Ost) M.Ost BSC ECON (Hons)

Colors
0094D4
00A9DD
6FCCEA
C7EBF8
E9F6FB

Requirements
Must have
• logo on the back
Nice to have
• Maybe a space for me to write an appointment time and date on the card.

```html
<!DOCTYPE html>
<html lang="en">
<head>
<meta charset="utf-8">
<title>Brookmere Osteopathy and Dry Needling – Business Card</title>
<link rel="stylesheet" href="https://fonts.googleapis.com/css2?family=Inter:wght@600;700&family=Montserrat:wght@300;400;500&display=swap">
<style>
  :root {
    --backdrop: #b5b5b5;
    --card-dark: #242424;
    --card-light: #ffffff;
    --brand-blue: #1e9ad6;
    --brand-orange: #f7922e;
    --ink: #161616;
    --ink-soft: #555555;
    --on-dark: #ffffff;
  }
  * { margin: 0; padding: 0; box-sizing: border-box; }
  html, body {
    width: 1200px; height: 1200px; overflow: hidden;
    background: var(--backdrop);
    font-family: "Montserrat", sans-serif;
  }
  .card {
    position: absolute; left: 179px; width: 861px; height: 496px;
  }
  .card-front { top: 84px; background: var(--card-dark); }
  .card-back { top: 622px; background: var(--card-light); overflow: hidden; }

  .brand-mark {
    position: absolute; border-radius: 50%;
    display: flex; align-items: center; justify-content: center; text-align: center;
    font-family: "Montserrat", sans-serif; font-weight: 500;
    text-transform: uppercase; letter-spacing: 2px; line-height: 1.4;
  }
  .card-front .brand-mark {
    left: 293px; top: 110px; width: 274px; height: 274px;
    border: 2px solid var(--on-dark); color: var(--on-dark); font-size: 20px;
  }
  .card-back .brand-mark {
    left: 21px; top: 56px; width: 230px; height: 230px;
    border: 2px solid var(--brand-blue); color: var(--brand-blue); font-size: 16px;
  }

  .identity {
    position: absolute; left: 270px; top: 70px;
    border-left: 3px solid var(--brand-orange); padding-left: 18px;
  }
  .person-name {
    font-family: "Inter", sans-serif; font-weight: 600; font-size: 31px;
    color: var(--ink); line-height: 1; margin-top: -4px;
  }
  .person-role {
    font-weight: 300; font-size: 27px; color: var(--ink-soft); line-height: 1; margin-top: 6px;
  }
  .person-credentials {
    font-weight: 400; font-size: 17px; color: var(--ink-soft); line-height: 1; margin-top: 10px;
  }

  .contacts {
    position: absolute; left: 270px; top: 196px;
    border-left: 3px solid var(--brand-orange); padding-left: 16px;
    list-style: none;
  }
  .contact-item {
    display: flex; align-items: center; height: 46px;
    color: var(--ink);
  }
  .contact-item svg { width: 26px; height: 26px; margin-right: 16px; flex: none; }
  .contact-item.web { font-size: 23.5px; }
  .web-accent { color: var(--brand-orange); }

  .appointment-title {
    position: absolute; right: 23px; top: 330px;
    font-family: "Inter", sans-serif; font-weight: 600; font-size: 29px; color: var(--ink);
  }
  .appointment-fields {
    position: absolute; left: 20px; top: 380px; right: 23px;
    display: flex; font-size: 26px; color: var(--ink);
  }
  .field { flex: 1; display: flex; align-items: baseline; }
  .field + .field { margin-left: 8px; }
  .field-line { flex: 1; border-bottom: 1.5px solid var(--ink); margin-left: 2px; height: 22px; }

  .address-band {
    position: absolute; left: 0; right: 0; bottom: 0; height: 60px;
    background: var(--card-dark); border-top: 5px solid var(--brand-orange);
    color: var(--on-dark); font-size: 26px;
    display: flex; align-items: center; justify-content: center;
  }
</style>
</head>
<body>
  <section class="card card-front">
    <div class="brand-mark">Brookmere<br>Osteopathy<br>and<br>Dry Needling</div>
  </section>

  <section class="card card-back">
    <div class="brand-mark">Brookmere<br>Osteopathy<br>and<br>Dry Needling</div>

    <div class="identity">
      <p class="person-name">Dr Marcus Penhallow</p>
      <p class="person-role">Osteopath</p>
      <p class="person-credentials">B.Clin.Sci (Ost) M.Ost BSc Econ (Hons)</p>
    </div>

    <ul class="contacts">
      <li class="contact-item web">
        <svg viewBox="0 0 24 24" fill="none" stroke="var(--brand-blue)" stroke-width="1.6" aria-hidden="true"><circle cx="12" cy="12" r="10"/><ellipse cx="12" cy="12" rx="4.5" ry="10"/><path d="M2 12h20M4 7h16M4 17h16M12 2v20"/></svg>
        <span>www.brookmere<span class="web-accent">osteopathyclinic</span>.example</span>
      </li>
    </ul>

    <p class="appointment-title">Next Appointment</p>
    <div class="appointment-fields">
      <div class="field">Date<span class="field-line"></span></div>
      <div class="field">Time<span class="field-line"></span></div>
    </div>

    <footer class="address-band">47 Lindcombe Lane Brookmere</footer>
  </section>
</body>
</html>
```